Business card design for Tolvin Waste

I would like double-sided business cards for myself and my partner that includes our logo and the existing colour scheme. We provide waste and environmental services to customers in the motor-vehicle and engineering industries.

```html
<!DOCTYPE html>
<html lang="en">
<head>
<meta charset="utf-8">
<title>Tolvin Waste – Business Card</title>
<link href="https://fonts.googleapis.com/css2?family=Montserrat:wght@500;700;800&display=swap" rel="stylesheet">
<style>
:root{
  --backdrop:#2a2a2a;
  --card:#242424;
  --lime:#a6d13a;
  --green:#6aaa3a;
  --white:#f2f2f2;
  --silver:#c9c9c9;
}
*{margin:0;padding:0;box-sizing:border-box}
html,body{width:1200px;height:895px;overflow:hidden;background:var(--backdrop)}
body{font-family:"Montserrat",Arial,sans-serif;color:var(--white);position:relative}
.card{position:absolute;width:580px;height:330px;background:var(--card);border-radius:18px;box-shadow:0 10px 30px rgba(0,0,0,.45);overflow:hidden}
.card--front{left:310px;top:100px}
.card--back{left:310px;top:465px}

/* front */
.front-brand{position:absolute;left:50px;top:50%;transform:translateY(-50%);display:flex;align-items:center;gap:22px}
.front-brand__mark{width:150px;height:150px;border-radius:50%;border:14px solid var(--lime)}
.front-brand__name{font-weight:800;font-size:42px;letter-spacing:1px;color:var(--silver);text-transform:uppercase;line-height:1.05}

/* back */
.back-brand{position:absolute;right:34px;top:30px;display:flex;align-items:center;gap:10px}
.back-brand__mark{width:34px;height:34px;border-radius:50%;border:4px solid var(--lime)}
.back-brand__name{font-weight:800;font-size:22px;color:var(--white);text-transform:uppercase}
.person{position:absolute;left:0;right:0;top:92px;text-align:center}
.person__name{font-weight:800;font-size:28px;color:var(--green)}
.person__role{font-weight:500;font-size:14px;letter-spacing:1px;margin-top:4px}
.divider{position:absolute;left:0;right:0;display:flex;justify-content:center;align-items:center;gap:8px}
.divider--icons{top:172px}
.divider--pin{top:262px}
.divider__rule{width:40px;height:2px;background:var(--green)}
.icon{width:28px;height:28px}
.contacts{position:absolute;left:0;right:0;top:210px;text-align:center;font-weight:500;font-size:13px;line-height:1.5}
.contacts .accent{color:var(--lime)}
.address{position:absolute;left:0;right:0;top:298px;text-align:center;font-weight:500;font-size:12px}
</style>
</head>
<body>

<section class="card card--front">
  <div class="front-brand">
    <div class="front-brand__mark"></div>
    <div class="front-brand__name">Tolvin<br>Waste</div>
  </div>
</section>

<section class="card card--back">
  <div class="back-brand">
    <div class="back-brand__mark"></div>
    <div class="back-brand__name">Tolvin Waste</div>
  </div>

  <div class="person">
    <div class="person__name">Marcus Delaney</div>
    <div class="person__role">Managing Partner</div>
  </div>

  <div class="divider divider--icons">
    <span class="divider__rule"></span>
    <svg class="icon" viewBox="0 0 28 28" aria-label="Phone"><circle cx="14" cy="14" r="12" fill="none" stroke="#6aaa3a" stroke-width="2"/><path d="M10 8l3 3-1.5 2a8 8 0 0 0 3.5 3.5l2-1.5 3 3-2 2c-5 0-10-5-10-10z" fill="#a6d13a"/></svg>
    <svg class="icon" viewBox="0 0 28 28" aria-label="Email"><circle cx="14" cy="14" r="12" fill="none" stroke="#6aaa3a" stroke-width="2"/><rect x="8" y="10" width="12" height="8" fill="#a6d13a"/><path d="M8 10l6 5 6-5" fill="none" stroke="#242424" stroke-width="1.3"/></svg>
    <svg class="icon" viewBox="0 0 28 28" aria-label="Website"><circle cx="14" cy="14" r="12" fill="none" stroke="#6aaa3a" stroke-width="2"/><circle cx="14" cy="14" r="6.5" fill="none" stroke="#a6d13a" stroke-width="1.5"/><path d="M7.5 14h13M14 7.5v13M10.5 9.5c2 3 2 6 0 9M17.5 9.5c-2 3-2 6 0 9" fill="none" stroke="#a6d13a" stroke-width="1.2"/></svg>
    <span class="divider__rule"></span>
  </div>

  <div class="contacts">
    <div>000-000-0000</div>
    <div>info@<span class="accent">tolvinwaste</span>.com</div>
    <div>www.<span class="accent">tolvinwaste</span>.com</div>
  </div>

  <div class="divider divider--pin">
    <span class="divider__rule"></span>
    <svg class="icon" viewBox="0 0 28 28" aria-label="Location"><circle cx="14" cy="14" r="12" fill="none" stroke="#6aaa3a" stroke-width="2"/><path d="M14 21s-5-5-5-9a5 5 0 0 1 10 0c0 4-5 9-5 9z" fill="#a6d13a"/><circle cx="14" cy="12" r="1.8" fill="#242424"/></svg>
    <span class="divider__rule"></span>
  </div>

  <div class="address">214 NW Ridge Ave. Suite 9, Salem, OR 97301</div>
</section>

</body>
</html>
```